New design of skin care labels for a natural makeup company

Our company sells 100% natural makeup and also offers a small selection of skin care cosmetics which aren't fully organic but have natural ingredients where possible and made by hand in small batches.
We are an English company with Japanese influence in that our staff and company name are Japanese, we understand how natural cosmetics in Japan are a huge business as demanded by Japanese girls and we include some Japanese ingredients in our cosmetics though we are marketing and selling in the UK.
We want to re-design the labels for 6 lines of our skin care range of cosmetics. These would be a mix of toners, creams, gels & face wash. There are 3 label sizes HxW:
50 x 120 mm
65 x 130 mm
90 x 115 mm
Our products are priced between £10-£15 so not expensive but not drug store budget prices either. We want the new labels to portray:
More luxury than common every day counter products
More natural than chemically preserved, fragranced, artificial products
Show they are free from parabens/sulphates and possibly even announce hand made in England
They need to include the usual necessary information like ingredients, usage instructions, warnings, weights, contact details along with our logo which is trademarked so unfortunately can't be altered or recoloured as its a mono logo.
We are open to all your ideas but our instincts will probably favour something clean/clear looking rather than fussy - though not too minimalist. Our bottles are either clear or semi transparent so we might prefer a see-thru label to show off the product. However these are just ideas at the moment and we may decide against them after seeing your various designs.
Females who care more about what they put on their skin.
Cosmetics

```html
<!DOCTYPE html>
<html lang="en">
<head>
<meta charset="UTF-8">
<title>KAORI Natural Face Care Moisturizer Label</title>
<link rel="stylesheet" href="https://fonts.googleapis.com/css2?family=Arimo:wght@400;700&display=swap">
<style>
  :root {
    --paper: #ffffff;
    --ink: #1e1b1a;
    --frame: #2a2a2a;
    --blush: #dc9487;
    --sand: #e6c9ad;
    --sand-soft: #f3e4d6;
    --sky-soft: #dcebf6;
  }
  html, body {
    margin: 0;
    padding: 0;
    width: 758px;
    height: 1200px;
    overflow: hidden;
    background: var(--paper);
  }
  .label {
    position: relative;
    width: 758px;
    height: 1200px;
    background: var(--paper);
    font-family: "Arimo", Arial, sans-serif;
    color: var(--ink);
  }
  .label__frame {
    position: absolute;
    left: 11px;
    top: 9px;
    width: 732px;
    height: 1178px;
    border: 2px solid var(--frame);
    box-sizing: border-box;
  }
  .label__tagline {
    position: absolute;
    top: 107px;
    left: 0;
    width: 100%;
    text-align: center;
    font-size: 29px;
    font-weight: 400;
    margin: 0;
  }
  .label__wash {
    position: absolute;
    left: 150px;
    top: 190px;
    width: 490px;
    height: 470px;
  }
  .label__brand {
    position: absolute;
    top: 692px;
    left: 0;
    width: 100%;
    text-align: center;
    font-size: 90px;
    font-weight: 400;
    letter-spacing: 2px;
    margin: 0;
    line-height: 1;
  }
  .label__product {
    position: absolute;
    top: 885px;
    left: 0;
    width: 100%;
    text-align: center;
    margin: 0;
    font-size: 28px;
    font-weight: 700;
    line-height: 37px;
    color: var(--blush);
  }
  .label__product-line--first {
    display: block;
    padding-right: 16px;
  }
  .label__product-line--second {
    display: block;
  }
</style>
</head>
<body>
  <main class="label">
    <div class="label__frame"></div>

    <p class="label__tagline">Natural face care</p>

    <svg class="label__wash" viewBox="0 0 490 470" role="img" aria-label="Soft watercolour wash in sand, cream and pale blue tones">
      <defs>
        <radialGradient id="washSand" cx="45%" cy="55%" r="55%">
          <stop offset="0%" stop-color="var(--sand)" stop-opacity="0.85"/>
          <stop offset="70%" stop-color="var(--sand-soft)" stop-opacity="0.8"/>
          <stop offset="100%" stop-color="var(--sand-soft)" stop-opacity="0"/>
        </radialGradient>
        <radialGradient id="washSky" cx="70%" cy="40%" r="45%">
          <stop offset="0%" stop-color="var(--sky-soft)" stop-opacity="0.9"/>
          <stop offset="100%" stop-color="var(--sky-soft)" stop-opacity="0"/>
        </radialGradient>
      </defs>
      <ellipse cx="250" cy="240" rx="240" ry="225" fill="url(#washSand)"/>
      <ellipse cx="320" cy="220" rx="170" ry="190" fill="url(#washSky)"/>
    </svg>

    <h1 class="label__brand">KAORI</h1>

    <p class="label__product">
      <span class="label__product-line--first">Natural</span>
      <span class="label__product-line--second">Face Care Moisturizer</span>
    </p>
  </main>
</body>
</html>
```